Hello my name is Colin, I am Starting a business called Harbor Health and fitness and am in need of a memorable business card.
It is a personal training studio. I have added the logo that i would like to be on the left center om my business card. i would like room left up the top for a heading sentence such as. "Is your body shocking for all the wrong reasons". there must be room left on the right of the logo below the main heading for 3 sub headings.
then under those 3 headings and logo room for another larger heading eg. "give me a call and learn how to eat chocolate, drink bear and have great sex". in what room is left i would like to be used for my contact details, use I'm Colin Pettersby your fitness expert on the left then on the right Phone, Email and website space in at least 12 Point. Very specific i know :) now onto the back, for the back i would like an eye catching graphic and room for one main headline and 3 bullet points centered just write anything i will choose what to put in them when i pick a winner. Thank you very much for sticking through all of that :) i appreciate you taking the time to read it and hopefully undergo designing me a business card.
I can't wait to see the designs!

Target Market(s)

slightly more towards females although it would probably be best if it was targeted towards both sexes

Industry/Entity Type

Training

Requirements
Nice to have
• I would love to see if anyone could come up with a design that would really make my card stand out and be memorable.
Should not have
• tacky fitness photos of abs and muscles etc.

```html
<!DOCTYPE html>
<html lang="en">
<head>
<meta charset="utf-8">
<title>Harbor Health and Fitness – Business Card</title>
<link rel="stylesheet" href="https://fonts.googleapis.com/css2?family=Didact+Gothic&family=PT+Sans&display=swap">
<style>
  :root {
    --brand-blue: #1d4f86;
    --brand-blue-deep: #123a66;
    --ink: #333333;
    --ink-soft: #444444;
    --charcoal: #303030;
    --card: #ffffff;
    --stage: #e9e6e2;
    --label: #1a1a1a;
  }
  * { margin: 0; padding: 0; box-sizing: border-box; }
  html, body { width: 1200px; height: 788px; overflow: hidden; }
  body {
    position: relative;
    background: var(--stage);
    font-family: "Didact Gothic", "Century Gothic", sans-serif;
    color: var(--ink);
  }
  .side-label {
    position: absolute;
    font-family: "PT Sans", Arial, sans-serif;
    font-size: 21px;
    color: var(--label);
    transform: translateX(-50%);
  }
  .card {
    position: absolute;
    width: 525px;
    height: 300px;
    background: var(--card);
    border-radius: 18px;
    box-shadow: 0 4px 12px rgba(0,0,0,0.25);
    overflow: hidden;
  }
  .card > * { position: absolute; }
  .brand-name { color: var(--brand-blue); line-height: 1; white-space: nowrap; }

  /* Front */
  .card-front { left: 337px; top: 74px; }
  .card-front .brand-word { left: 43px; top: 22px; font-size: 62px; }
  .card-front .brand-sub { left: 100px; top: 88px; font-size: 17px; }
  .card-front .headline { left: 293px; top: 46px; font-size: 17px; line-height: 22px; color: var(--ink); }
  .name-band { left: 0; top: 130px; width: 205px; height: 49px; display: flex; }
  .name-band .band-stub { width: 45px; background: var(--charcoal); }
  .name-band .band-main { flex: 1; background: var(--brand-blue); color: #fff; padding: 5px 0 0 1px; }
  .band-main .person { font-size: 17px; line-height: 21px; }
  .band-main .role { font-size: 12px; line-height: 16px; }
  .contact-list { left: 45px; top: 198px; list-style: none; }
  .contact-list li { display: flex; align-items: center; height: 28px; font-size: 20px; color: var(--ink); }
  .contact-list svg { width: 14px; height: 14px; margin-right: 11px; }
  .card-front .pitch { left: 293px; top: 188px; font-size: 17px; line-height: 22.5px; color: var(--ink); }

  /* Back 1 */
  .card-back-one { left: 53px; top: 446px; }
  .card-back-one .headline { left: 43px; top: 20px; font-size: 13px; line-height: 16px; color: var(--ink-soft); width: 185px; }
  .card-back-one .brand-word { left: 256px; top: 22px; font-size: 34px; }
  .card-back-one .brand-sub { left: 288px; top: 58px; font-size: 10px; }
  .figure-art {
    left: 40px; top: 78px; width: 122px; height: 207px;
    border-radius: 40px 40px 6px 6px;
    background: linear-gradient(180deg, var(--brand-blue), var(--brand-blue-deep));
  }
  .bullets { left: 258px; top: 116px; list-style: none; font-family: "PT Sans", Arial, sans-serif; font-size: 16px; color: #111; }
  .bullets li { height: 32px; display: flex; align-items: center; }
  .bullets li:nth-child(3) { margin-top: 4px; }
  .bullets li::before { content: ""; width: 5px; height: 5px; background: #111; margin-right: 19px; }
  .card-back-one .site { left: 257px; top: 254px; font-size: 20px; color: var(--ink); }

  /* Back 2 */
  .card-back-two { left: 621px; top: 441px; }
  .card-back-two .headline { left: 0; width: 100%; top: 20px; text-align: center; font-size: 13px; color: var(--ink-soft); }
  .card-back-two .brand-word { left: 0; width: 100%; text-align: center; top: 84px; font-size: 92px; }
  .card-back-two .brand-sub { left: 186px; top: 180px; font-size: 23px; }
  .card-back-two .site { left: 0; width: 100%; text-align: center; top: 253px; font-size: 20px; letter-spacing: 5px; color: var(--ink); }
</style>
</head>
<body>
  <div class="side-label" style="left:600px; top:34px;">Front</div>
  <div class="side-label" style="left:323px; top:404px;">Back - 1</div>
  <div class="side-label" style="left:897px; top:404px;">Back - 2</div>

  <section class="card card-front">
    <div class="brand-name brand-word">Harbor</div>
    <div class="brand-name brand-sub">Health and Fitness</div>
    <p class="headline">Is your body shocking<br>for all the wrong reasons</p>
    <div class="name-band">
      <div class="band-stub"></div>
      <div class="band-main">
        <div class="person">Colin Pettersby</div>
        <div class="role">Your Fitness Expert</div>
      </div>
    </div>
    <ul class="contact-list">
      <li><svg viewBox="0 0 14 14"><circle cx="7" cy="7" r="6" fill="none" stroke="#333" stroke-width="1"/><path d="M5 3.5 L6.3 5 L5.6 6 Q6.5 8 8 8.6 L9 7.8 L10.5 9 L9.6 10.4 Q5 9.5 3.8 4.6 Z" fill="#333"/></svg>+12 345 67890</li>
      <li><svg viewBox="0 0 14 14"><rect x="1" y="4" width="12" height="8" fill="#333"/><path d="M1 4 L7 9 L13 4" fill="none" stroke="#fff" stroke-width="1"/><path d="M3 4 L7 1 L11 4" fill="none" stroke="#333" stroke-width="1"/></svg>info@website.com</li>
      <li><svg viewBox="0 0 14 14" fill="none" stroke="#333" stroke-width="1"><circle cx="7" cy="7" r="6"/><ellipse cx="7" cy="7" rx="2.6" ry="6"/><path d="M1 7 H13 M2 4 H12 M2 10 H12"/></svg>www.website.com</li>
    </ul>
    <p class="pitch">Give me a call and learn<br>how to eat chocolate,<br>drink bear and have<br>great sex</p>
  </section>

  <section class="card card-back-one">
    <p class="headline">Is your body shocking for all the wrong reasons</p>
    <div class="brand-name brand-word">Harbor</div>
    <div class="brand-name brand-sub">Health and Fitness</div>
    <div class="figure-art" role="img" aria-label="Blue silhouette illustration of a man in a suit and a woman standing side by side"></div>
    <ul class="bullets">
      <li>Lorem Ipsum has been ...</li>
      <li>Lorem Ipsum has been ...</li>
      <li>Lorem Ipsum has been ...</li>
    </ul>
    <div class="site">www.website.com</div>
  </section>

  <section class="card card-back-two">
    <p class="headline">Is your body shocking for all the wrong reasons</p>
    <div class="brand-name brand-word">Harbor</div>
    <div class="brand-name brand-sub">Health and Fitness</div>
    <div class="site">www.website.com</div>
  </section>
</body>
</html>
```